Serviceleitfaden für das Hotel
Zielgruppe
Lindholms Hotel
Hallo,
ich brauch eine Serviceleitfaden in Form eines Flyers
Titelseite:
Logo , darunter den Begriff : Serviceleitfaden
Innenseite 1 Links:
Fernsehprogramme
1. KMT
2. BWX
3. NPQ
4. Dux 1
5. Via Zehner
6. Welle Vier
7. Jul
8. Funk 7
9. NPQ 2
ab 10 die Programme von Orbo
http://business.orbo-tv.de/obs/cms/de/hotel-zimmerloesung-basispaket.jsp
alle Sender außer Orbo 3D
Innenseite 1 Rechts, Innenseite 2 Links und Rechts
Serviceleitfaden
http://www.hotel-lindholms.de/de/zimmer/service-leitfaden
Rückseite:
Telefonnummern
Internet
Sie könne sich kostenlos bei Netzwerkfunkhaus über Wlan anmelden.
Danach müssen Sie nur Ihren Browser öffnen.
Anfahrskizze:
Siehe Bild
Druckformat:
http://www.papierwerk-online.de/tpl/holt-team/media/pdv/druckdatenskizzen/faltblatt__gefalzt_auf_din_a4__6-seiter_%28zickzackfalz%29_2.pdf
http://www.papierwerk-online.de/tpl/holt-team/media/pdv/druckdatenskizzen/faltblatt__gefalzt_auf_din_a4__6-seiter_%28zickzackfalz%29_1.pdf

```html
<!DOCTYPE html>
<html lang="de">
<head>
<meta charset="utf-8">
<title>Lindholms Hotel – Serviceleitfaden</title>
<link rel="stylesheet" href="https://fonts.googleapis.com/css2?family=Jost:wght@400;500;600&display=swap">
<style>
:root{
  --gold:#977d44;
  --ink:#1d1d1b;
  --paper:#ffffff;
  --bg:#ffffff;
  --map:#ede7da;
  --grey:#8a8a8a;
  --dark:#1f1f1f;
}
*{margin:0;padding:0;box-sizing:border-box}
html,body{width:1200px;height:848px;overflow:hidden;background:var(--bg)}
body{position:relative;font-family:"Jost",sans-serif;color:var(--ink)}
.sheet{position:absolute;background:var(--paper);box-shadow:0 1px 4px rgba(0,0,0,.18)}
.spread{left:60px;top:221px;width:711px;height:503px}
.band{position:absolute;left:0;top:0;width:100%;height:101px;background:var(--gold)}
.panel-title{position:absolute;top:66px;width:355px;text-align:center;color:#fff;font-weight:600;font-size:16px;letter-spacing:1.6px}
.panel-title.left{left:0}
.panel-title.right{left:356px}
.col{position:absolute;top:124px;width:112px;font-size:6.3px;line-height:9px}
.col h3{color:var(--gold);font-weight:600;font-size:7px;letter-spacing:.3px;line-height:9px}
.col p,.col ul{margin-bottom:9px}
.col ul{list-style:none}
.channels{position:absolute;left:46px;top:124px;list-style:none;font-weight:600;font-size:7px}
.channels li{height:18px;display:flex}
.channels .num{color:var(--gold);width:13px}
.orbo-note{position:absolute;left:46px;top:337px;font-size:7px;font-weight:600}
.orbo-name{position:absolute;left:46px;top:356px;font-size:17px;color:var(--grey);font-weight:400}
.orbo-sub{position:absolute;left:46px;top:391px;font-size:6.3px}
.footer-line{position:absolute;left:0;top:460px;width:100%;height:1.5px;background:var(--gold)}
.footer-brand{position:absolute;top:449px;width:100px;height:22px;background:var(--paper);display:flex;align-items:center;justify-content:center;gap:5px;color:var(--gold);font-size:9px;font-weight:500}
.footer-brand .dot{width:12px;height:12px;border-radius:50%;background:var(--dark)}
.back{left:790px;top:110px;width:355px;height:505px}
.back .band{height:96px}
.back-brand{position:absolute;left:0;top:30px;width:100%;display:flex;align-items:center;justify-content:center;gap:10px;color:#fff;font-size:22px;font-weight:400}
.back-brand .dot{width:36px;height:36px;border-radius:50%;background:var(--dark)}
.address{position:absolute;left:60px;top:184px;font-size:6.6px;line-height:9px;width:140px}
.address h4{color:var(--gold);font-weight:600;font-size:7px}
.address .phones{margin-top:14px}
.address .web{margin-top:12px;color:var(--gold);font-weight:600}
.internet{position:absolute;left:218px;top:200px;width:108px;font-size:6.6px;line-height:9px}
.internet h4{color:var(--gold);font-weight:600;font-size:7px}
.map{position:absolute;left:50px;top:290px;width:265px;height:145px;background:var(--map)}
.back-line{position:absolute;left:0;top:452px;width:100%;height:1.5px;background:var(--gold)}
</style>
</head>
<body>

<section class="sheet spread" aria-label="Innenseiten Fernsehprogramme">
  <div class="band"></div>
  <h2 class="panel-title left">FERNSEHPROGRAMME</h2>
  <h2 class="panel-title right">FERNSEHPROGRAMME</h2>

  <ol class="channels">
    <li><span class="num">1</span>KMT</li>
    <li><span class="num">2</span>BWX</li>
    <li><span class="num">3</span>NPQ</li>
    <li><span class="num">4</span>DUX 1</li>
    <li><span class="num">5</span>VIA ZEHNER</li>
    <li><span class="num">6</span>WELLE VIER</li>
    <li><span class="num">7</span>JUL</li>
    <li><span class="num">8</span>FUNK 7</li>
    <li><span class="num">9</span>NPQ 2</li>
  </ol>
  <p class="orbo-note">AB 10 DIE PROGRAMME VON</p>
  <p class="orbo-name">Orbo Business</p>
  <p class="orbo-sub">Alle Sender bis auf Orbo 3D</p>

  <div class="col" style="left:203px">
    <h3>ORBO CINEMA HD</h3>
    <p>Das Privatkino in Ihrem Hotelzimmer mit rund 20 deutschen TV-Premieren. Ob Komödie, Romanze, Science-Fiction oder Thriller.</p>
    <h3>ORBO ACTION HD</h3>
    <p>Hochspannung garantiert: 24 Stunden am Tag Adrenalin pur mit Action, Horror und Science-Fiction.</p>
    <h3>ORBO HITS HD</h3>
    <p>Die größten Kinohits der letzten Jahrzehnte mit allen technischen Vorteilen.</p>
    <h3>ORBO ATLANTIC HD</h3>
    <p>Die besten Produktionen von KVN, dem erfolgreichsten US-Premium-Sender, ausgewählte KVN-Filmhighlights und KVN-Dokumentationen. Alle Serien werden sowohl in Deutsch als auch in englischer Originalfassung verfügbar sein.</p>
    <h3>ORBO SPORT NEWS HD</h3>
    <p>Mit Orbo Sport News bleiben Sie im weltweiten Sportgeschehen immer auf dem Laufenden. Der einzige Sender in Deutschland und Österreich, der täglich 24 Stunden Sportnachrichten live präsentiert.</p>
  </div>

  <div class="col" style="left:401px">
    <h3>ORBO SPORT HD1 + HD2</h3>
    <ul>
      <li>· Europäische Meisterliga: live</li>
      <li>· Nationaler Pokal: live</li>
      <li>· Kontinental-Liga: live</li>
      <li>· Englische Liga: live</li>
      <li>· Golf: Nordamerika-Tour und Europa-Tour</li>
      <li>· Tour sowie alle vier Major-Turniere und der Atlantik-Cup</li>
      <li>· Tennis vom Rasenturnier</li>
      <li>· Königsklasse im Motorsport</li>
    </ul>
    <h3>ORBO SPORT AUSTRIA</h3>
    <p>Auf Orbo Sport Austria sind alle Spiele der österreichischen Oberliga und der Zweiten Liga für Sie erhältlich. Top-Klubs wie FC Salzachtal, SV Donaustadt oder Wiener Kickers live, das Live-Magazin „Tor und Tat“ und Top-Begegnungen der Basketball-Oberliga – alles live.</p>
    <h3>ORBO FUSSBALL HD1 + HD2</h3>
    <p>Der Klassiker für echte Fußballfans: Die erste und zweite Fußball-Liga live und in HD sowie Konferenzschaltung bei Parallelspielen der ersten und zweiten Liga</p>
    <h3>MERIDIAN SERIEN HD</h3>
    <p>Exklusiven Serien als deutsche TV-Premieren und mitreißenden Blockbustern.</p>
  </div>

  <div class="col" style="left:559px">
    <h3>TERRA EXPLORER<br>CHANNEL HD</h3>
    <p>Für echte Entdecker mit faszinierenden Bildern, packenden Geschichten und informativen Dokumentationen, von den entlegensten Winkeln der Welt bis zu den Zentren der Moderne.</p>
    <h3>TERRA WILD HD</h3>
    <p>Faszinierende Natur und Tierwelt. Von fernen Naturparadiesen dieser Erde und den Tiefen der Ozeane bis hin zu Europas Naturparks.</p>
    <h3>VULPA HD</h3>
    <p>Preisgekrönte Top-Serien als deutsche TV-Erstausstrahlung sowie Thriller-, Kult- und Comedyserien,</p>
    <h3>FAMILIA CHANNEL HD</h3>
    <p>Zeichentrick-Klassiker und die neuesten Animations-Filmhighlights. Perfekte TV-Unterhaltung für die ganze Familie.</p>
    <h3>LÖWENFILM CHANNEL HD</h3>
    <p>Besten Filmhighlights aus der großen Traumfabrik in brillantem HD, unvergessliche Klassiker, beliebte Blockbuster, erfolgreiche Filmreihen und preisgekrönte Lieblingsstreifen.</p>
  </div>

  <div class="footer-line"></div>
  <div class="footer-brand" style="left:127px">Lindholms Hotel<span class="dot"></span></div>
  <div class="footer-brand" style="left:483px">Lindholms Hotel<span class="dot"></span></div>
</section>

<section class="sheet back" aria-label="Rückseite Kontakt und Anfahrt">
  <div class="band"></div>
  <div class="back-brand">Lindholms Hotel<span class="dot"></span></div>

  <div class="address">
    <h4>Lindholms Hotel Hallborg</h4>
    <p>Jonas Lindholm<br>Lange Gasse 27<br>49811 Hallborg Deutschland</p>
    <p class="phones">Telefon: +49 (0) 5512-40617<br>Telefax: +49 (0) 5512-406170</p>
    <p class="web">www.hotel-lindholms.de</p>
  </div>

  <div class="internet">
    <h4>Internet:</h4>
    <p>Sie könne sich kostenlos bei Netzwerkfunkhaus über Wlan anmelden. Danach müssen Sie nur Ihren Browser öffnen.</p>
  </div>

  <div class="map" role="img" aria-label="Anfahrtsskizze mit Straßen zum Hotel und Hinweis auf den Hotelparkplatz"></div>
  <div class="back-line"></div>
</section>

</body>
</html>
```